Financial Services Business Card Design

We are a financial services company Based in London, offering Short term Funding Solutions for companies, raising anywhere between £20,000 and £25million pounds.

The Card must have a professional look as it is going to be handed out to professionals I.E Solicitors, Accountants, Company directors and Business owners.

See Attached our company Logo

Industry/Entity Type

Business

Contact Information for Business Card

Lewis Thorncroft
Suite 41
R K House
Bramblecote Lane
Kestrelford
HP19 4QX

```html
<!DOCTYPE html>
<html lang="en">
<head>
<meta charset="utf-8">
<title>Harbourline Capital – Business Card</title>
<link rel="stylesheet" href="https://fonts.googleapis.com/css2?family=Arimo:wght@400;700&display=swap">
<style>
  :root {
    --backdrop: #e9eaec;
    --card-blue: #1c68ae;
    --accent-green: #3a9a2c;
    --paper-white: #f3f4f5;
    --ink-white: #ffffff;
    --card-shadow: rgba(40, 60, 90, 0.18);
  }
  * { margin: 0; padding: 0; box-sizing: border-box; }
  html, body {
    width: 1200px;
    height: 900px;
    overflow: hidden;
    background: var(--backdrop);
    font-family: "Arimo", Arial, sans-serif;
  }
  .card-set {
    position: absolute;
    inset: 0;
    display: flex;
    align-items: center;
    justify-content: center;
    gap: 48px;
  }
  .card {
    position: relative;
    width: 520px;
    height: 298px;
    border-radius: 3px;
    overflow: hidden;
    background: var(--card-blue);
    box-shadow: 0 14px 30px var(--card-shadow);
  }
  .card-front__curve {
    position: absolute;
    inset: 0;
    width: 100%;
    height: 100%;
  }
  .card-front__curve .band-green { fill: var(--accent-green); }
  .card-front__curve .cap-white { fill: var(--paper-white); }
  .brand {
    position: absolute;
    left: 0;
    right: 0;
    top: 112px;
    display: flex;
    align-items: center;
    justify-content: center;
    gap: 10px;
  }
  .brand__dot {
    width: 22px;
    height: 22px;
    border-radius: 50%;
    background: var(--card-blue);
  }
  .brand__name {
    font-weight: 700;
    font-size: 30px;
    letter-spacing: 0.5px;
    color: var(--card-blue);
    text-transform: uppercase;
  }
  .holder-name {
    position: absolute;
    left: 0;
    right: 0;
    top: 236px;
    text-align: center;
    font-weight: 700;
    font-size: 15px;
    letter-spacing: 0.5px;
    color: var(--ink-white);
    text-transform: uppercase;
  }
  .card-back {
    display: flex;
    flex-direction: column;
    align-items: center;
    justify-content: center;
    gap: 16px;
    color: var(--ink-white);
  }
  .card-back__dot {
    width: 40px;
    height: 40px;
    border-radius: 50%;
    background: var(--ink-white);
  }
  .address {
    font-style: normal;
    font-weight: 700;
    font-size: 15px;
    line-height: 1.3;
    text-align: center;
  }
</style>
</head>
<body>
  <main class="card-set">
    <section class="card card-front" aria-label="Business card front">
      <svg class="card-front__curve" viewBox="0 0 520 298" preserveAspectRatio="none" aria-hidden="true">
        <ellipse class="band-green" cx="250" cy="20" rx="330" ry="210"/>
        <ellipse class="cap-white" cx="250" cy="14" rx="322" ry="204"/>
      </svg>
      <div class="brand">
        <span class="brand__dot"></span>
        <span class="brand__name">Harbourline Capital</span>
      </div>
      <p class="holder-name">Lewis Thorncroft</p>
    </section>

    <section class="card card-back" aria-label="Business card back">
      <span class="card-back__dot"></span>
      <address class="address">
        Suite 41, R K House, Bramblecote Lane,<br>
        Kestrelford, HP19 4QX
      </address>
    </section>
  </main>
</body>
</html>
```